Pale Lanterns Old Lane Walk Poster Design

We need an A4 sized poster to promote our weekly true crime tours. This poster will be posted onto community noticeboards.
Lots of information and images can be viewed at the following links:-
www.palelanterns.com.au
www.palelanterns.com.au/bookings/
https://www.facebook.com/palelanternsoldlane/
https://www.examplereviews.com.au/Attraction_Review-g000000-d00000000-Reviews-Pale_Lanterns-Newcastle_Greater_Newcastle_New_South_Wales.html
There are also a number of images for possible use at the following link - we are open to intepretation:-
http://palelanterns.com.au/tour-photographs/
The font on our website is "SpecialElite" so we would like to continue using that font type.
Target Market(s)
Adults 25-65.
Font styles to use
Other font styles liked:
- Special Elite
Colors
Designer to choose colors to be used in the design.
Look and feel
Each slider illustrates characteristics of the customer's brand and the style your logo design should communicate.

```html
<!DOCTYPE html>
<html lang="en">
<head>
<meta charset="utf-8">
<title>Pale Lanterns Old Lane Walk – Poster</title>
<link href="https://fonts.googleapis.com/css2?family=Special+Elite&family=Courier+Prime:wght@400;700&family=Raleway:wght@400;500;600;700;800&display=block" rel="stylesheet">
<style>
  :root {
    --ink: #0d0d0d;
    --night: #1a1a1a;
    --paper: #ffffff;
    --blood: #e3110f;
    --band: #e0120e;
    --rule: #9a9a9a;
    --typewriter: "Special Elite", "Courier Prime", "Courier New", monospace;
  }
  * { margin: 0; padding: 0; box-sizing: border-box; }
  html, body { width: 856px; height: 1200px; overflow: hidden; background: var(--ink); }
  .poster {
    position: relative;
    width: 856px; height: 1200px;
    overflow: hidden;
    background: linear-gradient(180deg, #0c0c0c 0%, #151515 20%, #262626 34%, #1a1a1a 100%);
    color: var(--paper);
    font-family: "Raleway", sans-serif;
  }
  .street-scene {
    position: absolute; left: 0; top: 380px; width: 640px; height: 640px;
    background:
      radial-gradient(ellipse 180px 90px at 28% 74%, rgba(10,10,10,.75) 0%, rgba(10,10,10,0) 100%),
      radial-gradient(ellipse 40px 80px at 74% 83%, rgba(5,5,5,.8) 0%, rgba(5,5,5,0) 100%),
      radial-gradient(ellipse 300px 200px at 48% 55%, rgba(175,175,175,.55) 0%, rgba(120,120,120,.2) 55%, rgba(0,0,0,0) 100%),
      radial-gradient(ellipse 260px 160px at 20% 30%, rgba(110,110,110,.45) 0%, rgba(0,0,0,0) 100%),
      linear-gradient(180deg, rgba(40,40,40,0) 0%, #4c4c4c 22%, #5e5e5e 50%, #3a3a3a 78%, rgba(26,26,26,0) 100%);
  }
  .street-scene::after {
    content: ""; position: absolute; inset: 0;
    background: linear-gradient(90deg, rgba(26,26,26,0) 70%, #1d1d1d 100%);
  }
  .title {
    position: absolute; left: 0; top: 52px; width: 856px;
    text-align: center;
    font-family: var(--typewriter);
    font-weight: 400;
    font-size: 90px; line-height: 96px;
    color: var(--blood);
  }
  .band {
    position: absolute; left: 0; top: 150px; width: 856px; height: 74px;
    background: var(--band);
    text-align: center;
    font-family: var(--typewriter);
    font-size: 74px; line-height: 80px;
    color: var(--paper);
  }
  .tagline {
    position: absolute; left: 0; top: 240px; width: 856px;
    text-align: center;
    font-family: var(--typewriter);
    font-size: 30px; line-height: 36px; color: var(--paper);
  }
  .rule { position: absolute; left: 37px; width: 782px; height: 1px; background: var(--rule); }
  .rule--top { top: 298px; }
  .rule--bottom { top: 408px; }
  .headline {
    position: absolute; left: 0; top: 316px; width: 856px;
    text-align: center;
    font-weight: 700; font-size: 37px; line-height: 38px;
    letter-spacing: -0.8px; text-transform: uppercase;
  }
  .highlights {
    position: absolute; left: 36px; top: 432px; width: 520px;
    list-style: none;
    font-weight: 600; font-size: 15.5px; line-height: 28px;
    z-index: 2;
  }
  .highlights li { position: relative; padding-left: 16px; }
  .highlights li::before { content: "•"; position: absolute; left: 0; font-size: 11px; }
  .snapshot {
    position: absolute;
    background: var(--paper);
    padding: 7px;
    box-shadow: 0 4px 12px rgba(0,0,0,.6);
    z-index: 2;
  }
  .snapshot div { width: 100%; height: 100%; }
  .snapshot--moonlit { left: 560px; top: 444px; width: 260px; height: 186px; transform: rotate(1.5deg); }
  .snapshot--moonlit div { background: linear-gradient(180deg, #1d2f8c 0%, #2b3f9a 45%, #b69a48 70%, #2d2d23 100%); }
  .snapshot--street { left: 542px; top: 608px; width: 258px; height: 168px; transform: rotate(-1deg); }
  .snapshot--street div { background: linear-gradient(180deg, #d9dcd2 0%, #8a6a52 35%, #6e6c68 65%, #4a4a44 100%); }
  .snapshot--harbour { left: 562px; top: 774px; width: 258px; height: 184px; transform: rotate(0.8deg); }
  .snapshot--harbour div { background: linear-gradient(180deg, #dcdccb 0%, #b9c6a0 40%, #6f8f52 70%, #a9b77d 100%); }
  .price {
    position: absolute; left: 70px; top: 842px; width: 140px; height: 140px;
    border-radius: 50%; background: var(--blood);
    text-align: center; color: var(--paper);
    font-size: 11.5px; line-height: 13px;
    z-index: 2;
  }
  .price__amount { display: block; margin-top: 18px; font-weight: 800; font-size: 30px; line-height: 34px; }
  .price__label { display: block; font-weight: 700; font-style: italic; margin-top: 3px; }
  .brand {
    position: absolute; left: 248px; top: 880px; width: 360px; height: 210px;
    border-radius: 50%;
    background: radial-gradient(ellipse at center, #131313 0%, #131313 62%, rgba(19,19,19,0) 72%);
    z-index: 1;
  }
  .brand__name {
    position: absolute; left: 0; top: 1014px; width: 856px;
    text-align: center;
    font-weight: 600; font-size: 33px; line-height: 40px; letter-spacing: 0.5px;
    color: var(--paper);
    z-index: 2;
  }
  .booking {
    position: absolute; left: 0; top: 1078px; width: 856px;
    text-align: center;
    font-family: var(--typewriter);
  }
  .booking__phone-line { font-size: 42px; line-height: 48px; }
  .booking__phone { color: var(--blood); }
  .booking__email { font-size: 27px; line-height: 32px; }
</style>
</head>
<body>
<main class="poster">
  <div class="street-scene" role="img" aria-label="Misty black and white street scene with a tram and a lone figure in the rain"></div>

  <h1 class="title">Pale Lanterns</h1>
  <div class="band">Old Lane Walk</div>
  <p class="tagline">.......stories the city tried to forget.......</p>

  <div class="rule rule--top"></div>
  <h2 class="headline">Take a walk on the dark side<br>revisit the scenes of the crimes.</h2>
  <div class="rule rule--bottom"></div>

  <ul class="highlights">
    <li>Retrace the steps of Newcastle's most infamous murderers.</li>
    <li>Descend into the murky world of fraudsters, adulterers<br>&nbsp;and lordly impersonators.</li>
    <li>Unearth the keys to the heart of the Tomahawk Murderer.</li>
    <li>Relive a time that proves truth is far stranger than fiction.</li>
    <li>Book your ticket for a unique investigation into a dark<br>&nbsp;and crime ridden history.</li>
  </ul>

  <figure class="snapshot snapshot--moonlit"><div role="img" aria-label="Historic station building at night under a red full moon"></div></figure>
  <figure class="snapshot snapshot--street"><div role="img" aria-label="Vintage city main street with buses and parked cars"></div></figure>
  <figure class="snapshot snapshot--harbour"><div role="img" aria-label="Early colonial painting of a green harbour coastline"></div></figure>

  <div class="price">
    <span class="price__amount">$34.00</span>
    <span class="price__label">Duration:</span>
    90 Minutes (approx)
    <span class="price__label">Location:</span>
    Newcastle East,<br>NSW
  </div>

  <div class="brand"></div>
  <div class="brand__name">PALE LANTERNS</div>

  <div class="booking">
    <p class="booking__phone-line">Book Now: <span class="booking__phone">0491570156</span></p>
    <p class="booking__email">Email: info@palelanterns.com.au</p>
  </div>
</main>
</body>
</html>
```